Business Card Design

I give lessons and clinics for dressage riders
I would like the design to be an outline (with broad lines) of a dressage horse and rider with in background of whole card with print over top tan or parchment card with burgundy print

Industry/Entity Type

Business

Contact Information for Business Card

Ned Carrow
617-354-2790
Classical dressage training for the modern American
Clinics, lessons, training level -Prix St. George

Requirements
Must have
• broad lined outline of dressage horse and rider

```html
<!DOCTYPE html>
<html lang="en">
<head>
<meta charset="utf-8">
<title>Ned Carrow — Business Card</title>
<link rel="stylesheet" href="https://fonts.googleapis.com/css2?family=Alfa+Slab+One&family=Tinos:ital@1&display=swap">
<style>
  :root {
    --burgundy: #6e1218;
    --burgundy-light: #8a2a33;
    --burgundy-dark: #2c0507;
    --card-white: #ffffff;
    --ink-white: #ffffff;
    --ink-dark: #2a0a0c;
    --sketch-light: #e6c9cc;
    --sketch-mid: #c08e94;
    --rail: #e9dadb;
  }
  html, body {
    margin: 0;
    padding: 0;
    overflow: hidden;
    background: var(--card-white);
  }
  .card {
    position: relative;
    width: 1200px;
    height: 702px;
    overflow: hidden;
    background: var(--card-white);
  }
  .card__band {
    position: absolute;
    left: 0;
    top: 0;
    width: 1200px;
    height: 469px;
    background:
      radial-gradient(ellipse 55% 45% at 62% 40%, var(--burgundy-light) 0%, transparent 70%),
      radial-gradient(ellipse 40% 35% at 25% 30%, rgba(140,40,50,0.6) 0%, transparent 70%),
      radial-gradient(ellipse 90% 80% at 50% 45%, var(--burgundy) 30%, var(--burgundy-dark) 100%);
  }
  .card__illustration {
    position: absolute;
    left: 46px;
    top: 105px;
    width: 516px;
    height: 300px;
  }
  .card__text {
    position: absolute;
    transform: translateX(-50%);
    white-space: nowrap;
    margin: 0;
    color: var(--ink-white);
    line-height: 1;
  }
  .card__name {
    left: 812px;
    top: 100px;
    font-family: "Alfa Slab One", Georgia, serif;
    font-weight: 400;
    font-size: 60px;
    letter-spacing: 2px;
  }
  .card__line {
    font-family: "Tinos", "Times New Roman", serif;
    font-style: italic;
    font-size: 44px;
    letter-spacing: 2px;
  }
  .card__line--tagline1 { top: 190px; left: 810px; }
  .card__line--tagline2 { top: 246px; left: 808px; }
  .card__line--clinics  { top: 302px; left: 784px; }
  .card__line--lessons  { top: 356px; left: 791px; }
  .card__line--levels   { top: 409px; left: 810px; }
  .card__contact {
    position: absolute;
    left: 603px;
    top: 526px;
    transform: translateX(-50%) scaleX(0.78);
    white-space: nowrap;
    margin: 0;
    font-family: "Tinos", "Times New Roman", serif;
    font-style: italic;
    font-size: 72px;
    line-height: 1;
    color: var(--ink-dark);
  }
</style>
</head>
<body>
  <div class="card">
    <div class="card__band"></div>

    <svg class="card__illustration" viewBox="0 0 516 300" role="img" aria-label="Outline drawing of a horse and rider clearing a jump rail">
      <defs>
        <radialGradient id="sketch-fill" cx="45%" cy="42%" r="55%">
          <stop offset="0%" stop-color="var(--sketch-light)" stop-opacity="0.75"/>
          <stop offset="60%" stop-color="var(--sketch-mid)" stop-opacity="0.45"/>
          <stop offset="100%" stop-color="var(--sketch-mid)" stop-opacity="0"/>
        </radialGradient>
      </defs>
      <ellipse cx="230" cy="140" rx="210" ry="150" fill="url(#sketch-fill)"/>
      <line class="rail" x1="0" y1="238" x2="516" y2="238" stroke="var(--rail)" stroke-width="3"/>
      <line class="rail" x1="0" y1="251" x2="516" y2="251" stroke="var(--rail)" stroke-width="3"/>
    </svg>

    <h1 class="card__text card__name">Ned Carrow</h1>
    <p class="card__text card__line card__line--tagline1">Classical dressage training</p>
    <p class="card__text card__line card__line--tagline2">for the modern American</p>
    <p class="card__text card__line card__line--clinics">Clinics</p>
    <p class="card__text card__line card__line--lessons">Lessons</p>
    <p class="card__text card__line card__line--levels">Training level -Prix St. George</p>

    <p class="card__contact">Contact No. : 617-354-2790</p>
  </div>
</body>
</html>
```